3 x Geometric Mandalas for a Nutritional Supplement Label

I have a nutritional supplement company that will use 3 Geometric style Mandalas on the label. These needs to be fully colored using bright colors.

The logo is attached and I want something that is in keeping with the logo - its almost like stained glass and fractured / geometric. So if somehow we can combine a mandala with stained glass style lines and less detail than is usually in a mandala that is what I want.

I prefer these to be circular (but am open to alternate submissions) - but each one can be different as long as they work well together cohesively.

Perhaps the 3 can be different shades of colors, one greens, one pinks / purples, one blues or something like that.

Target Market(s)

Women 30-60 years old

Industry/Entity Type

Nutrition

Contact Information for Business Card

The business card needs to have the Mandalas / graphics as well as the following information:

Pella Roux
CEO | Founder

+1 555 318 4920

pella@solmerico.com
www.solmerico.com

Font styles to use
Sans Serif
Decorative

Requirements
Must have
• Colors! bright pretty colors!
• The business card needs to have the logo (ai attached) in the middle on one side, with one of the mandalas set to one side. The other side with the information and one or two of the mandalas also off set
Nice to have
• cohesive mandalas

```html
<!DOCTYPE html>
<html lang="en">
<head>
<meta charset="utf-8">
<title>Solmerico Business Cards</title>
<link rel="stylesheet" href="https://fonts.googleapis.com/css2?family=Jost:wght@300;400&display=swap">
<style>
  :root {
    --sun: #fdc46e;
    --orchid: #b85e90;
    --mint: #86dfc8;
    --paper: #ffffff;
    --ink: #2b2b2b;
    --bg-light: #efede6;
    --bg-dark: #d3cecd;
    --shadow: 6px 8px 10px rgba(60, 50, 50, 0.28);
  }
  * { box-sizing: border-box; margin: 0; padding: 0; }
  html, body { width: 1200px; height: 840px; overflow: hidden; }
  body {
    position: relative;
    background: linear-gradient(135deg, var(--bg-light) 0%, var(--bg-dark) 100%);
    font-family: "Jost", sans-serif;
    font-weight: 300;
    color: var(--ink);
  }

  /* ---------- Contact cards ---------- */
  .contact-card {
    position: absolute;
    box-shadow: var(--shadow);
    text-align: center;
    border: calc(7 * var(--u)) solid var(--accent);
  }
  .contact-card--framed { background: var(--paper); }
  .contact-card--solid { background: var(--accent); }
  .contact-card--large { --u: 1px; width: 231px; height: 323px; }
  .contact-card--small { --u: 0.63px; width: 146px; height: 202px; }
  .contact-card--sun { --accent: var(--sun); }
  .contact-card--orchid { --accent: var(--orchid); }
  .contact-card--mint { --accent: var(--mint); }

  .contact-card > * {
    position: absolute;
    left: 0; right: 0;
    line-height: 1;
    white-space: nowrap;
    transform: translateY(-50%);
  }
  .brand-mark {
    top: calc(64 * var(--u));
    font-size: calc(9 * var(--u));
    font-weight: 400;
    letter-spacing: 0.3em;
    margin-right: -0.3em;
  }
  .holder-name {
    top: calc(127 * var(--u));
    font-size: calc(19 * var(--u));
    font-weight: 300;
    letter-spacing: 0.2em;
    margin-right: -0.2em;
  }
  .holder-role {
    top: calc(146 * var(--u));
    font-size: calc(8 * var(--u));
    letter-spacing: 0.18em;
    margin-right: -0.18em;
    color: var(--accent);
  }
  .holder-phone {
    top: calc(188 * var(--u));
    font-size: calc(10 * var(--u));
    letter-spacing: 0.16em;
    margin-right: -0.16em;
  }
  .holder-email {
    top: calc(204 * var(--u));
    font-size: calc(7.5 * var(--u));
    letter-spacing: 0.2em;
    margin-right: -0.2em;
  }
  .holder-web {
    top: calc(268 * var(--u));
    font-size: calc(8.5 * var(--u));
    letter-spacing: 0.4em;
    margin-right: -0.4em;
    color: var(--accent);
  }
  .contact-card--solid .holder-role { color: rgba(255,255,255,0.75); }
  .contact-card--solid .holder-web { color: rgba(255,255,255,0.85); }

  /* ---------- Mandala label cards ---------- */
  .label-card {
    position: absolute;
    top: 355px;
    width: 231px;
    height: 323px;
    background: var(--paper);
    border: 6px solid var(--accent);
    box-shadow: var(--shadow);
    text-align: center;
  }
  .label-card--sun { left: 359px; --accent: var(--sun); --m1: #2d9dbd; --m2: #fbc46d; --m3: #86dfc8; }
  .label-card--orchid { left: 611px; --accent: var(--orchid); --m1: #3b4a8f; --m2: #b85e90; --m3: #2d9dbd; }
  .label-card--mint { left: 863px; --accent: var(--mint); --m1: #fbc46d; --m2: #86dfc8; --m3: #c8f0de; }

  .mandala-art {
    position: absolute;
    top: 0; left: 0;
    width: 100%;
    height: 210px;
    background:
      radial-gradient(circle at 50% 34%, var(--m2) 0 12%, transparent 13%),
      radial-gradient(ellipse at 50% 30%, var(--m3) 0%, var(--m1) 62%, transparent 63%),
      linear-gradient(180deg, var(--m1) 0%, var(--m3) 55%, var(--paper) 100%);
  }
  .label-brand {
    position: absolute;
    left: 0; right: 0;
    top: 236px;
    display: flex;
    flex-direction: column;
    align-items: center;
    gap: 12px;
  }
  .label-brand__dot {
    width: 22px; height: 22px;
    border-radius: 50%;
    background: var(--ink);
  }
  .label-brand__name {
    font-size: 17px;
    font-weight: 400;
    letter-spacing: 0.42em;
    margin-right: -0.42em;
  }
</style>
</head>
<body>

  <!-- Large contact cards -->
  <article class="contact-card contact-card--large contact-card--framed contact-card--sun" style="left:63px; top:73px;">
    <p class="brand-mark">SOLMERICO</p>
    <h2 class="holder-name">PELLA ROUX</h2>
    <p class="holder-role">CEO &amp; Founder</p>
    <p class="holder-phone">+1 555 318 4920</p>
    <p class="holder-email">pella@solmerico.com</p>
    <p class="holder-web">WWW.SOLMERICO.COM</p>
  </article>

  <article class="contact-card contact-card--large contact-card--solid contact-card--sun" style="left:63px; top:428px;">
    <p class="brand-mark">SOLMERICO</p>
    <h2 class="holder-name">PELLA ROUX</h2>
    <p class="holder-role">CEO &amp; Founder</p>
    <p class="holder-phone">+1 555 318 4920</p>
    <p class="holder-email">pella@solmerico.com</p>
    <p class="holder-web">WWW.SOLMERICO.COM</p>
  </article>

  <!-- Small contact cards -->
  <article class="contact-card contact-card--small contact-card--framed contact-card--orchid" style="left:491px; top:122px;">
    <p class="brand-mark">SOLMERICO</p>
    <h2 class="holder-name">PELLA ROUX</h2>
    <p class="holder-role">CEO &amp; Founder</p>
    <p class="holder-phone">+1 555 318 4920</p>
    <p class="holder-email">pella@solmerico.com</p>
    <p class="holder-web">WWW.SOLMERICO.COM</p>
  </article>

  <article class="contact-card contact-card--small contact-card--solid contact-card--orchid" style="left:654px; top:122px;">
    <p class="brand-mark">SOLMERICO</p>
    <h2 class="holder-name">PELLA ROUX</h2>
    <p class="holder-role">CEO &amp; Founder</p>
    <p class="holder-phone">+1 555 318 4920</p>
    <p class="holder-email">pella@solmerico.com</p>
    <p class="holder-web">WWW.SOLMERICO.COM</p>
  </article>

  <article class="contact-card contact-card--small contact-card--framed contact-card--mint" style="left:828px; top:122px;">
    <p class="brand-mark">SOLMERICO</p>
    <h2 class="holder-name">PELLA ROUX</h2>
    <p class="holder-role">CEO &amp; Founder</p>
    <p class="holder-phone">+1 555 318 4920</p>
    <p class="holder-email">pella@solmerico.com</p>
    <p class="holder-web">WWW.SOLMERICO.COM</p>
  </article>

  <article class="contact-card contact-card--small contact-card--solid contact-card--mint" style="left:991px; top:122px;">
    <p class="brand-mark">SOLMERICO</p>
    <h2 class="holder-name">PELLA ROUX</h2>
    <p class="holder-role">CEO &amp; Founder</p>
    <p class="holder-phone">+1 555 318 4920</p>
    <p class="holder-email">pella@solmerico.com</p>
    <p class="holder-web">WWW.SOLMERICO.COM</p>
  </article>

  <!-- Mandala label cards -->
  <article class="label-card label-card--sun">
    <div class="mandala-art" role="img" aria-label="Geometric stained-glass mandala in teal, mint and yellow with a pink star centre"></div>
    <div class="label-brand">
      <span class="label-brand__dot"></span>
      <span class="label-brand__name">SOLMERICO</span>
    </div>
  </article>

  <article class="label-card label-card--orchid">
    <div class="mandala-art" role="img" aria-label="Geometric stained-glass mandala in indigo, purple, pink and teal with a mint star centre"></div>
    <div class="label-brand">
      <span class="label-brand__dot"></span>
      <span class="label-brand__name">SOLMERICO</span>
    </div>
  </article>

  <article class="label-card label-card--mint">
    <div class="mandala-art" role="img" aria-label="Geometric stained-glass mandala in yellow and mint greens with a pink star centre"></div>
    <div class="label-brand">
      <span class="label-brand__dot"></span>
      <span class="label-brand__name">SOLMERICO</span>
    </div>
  </article>

</body>
</html>
```